Church Equipping Classes Needing Printed Banner

We are looking for a printed Banner that will be 24x36. I attached and example on the brief. Please visit out website at brenlux.org to see what we do.

Summit Path is the name of our equipping process. It has four classes:

Summit Path - The end goal is to Connect
Harvest Rhythm - Our end goal is for people to get the Culture of the Kingdom
Table of Embers - End goal is they would find Community
Missions - Out-Reachers End goal is they would go on missions.

Our mission is teaching people and reaching nations with the message of Freedom. Galatians 5:1

The concept/idea behind the banner is to communicate this mission as well as the four classes.

Logos to incorporate:
Attached

Please let me know of anything you need to help. We would like our logo on everything but an idea to incorporate the whole concept of Summit Path. Then each class represented as well in that concept. These four classes run each month at our church and each one will have it's on banner and book cover, etc.

The text that the banner should contain is:

Teaching people, Reaching Nations with Freedom.
Galatians 5:1

- Encounter the radical grace & supernatural love of your Heavenly Father!
- Learn something practical and relevant that's guaranteed to work on Sunday AND Monday!
- Connect with others like you- people walking from brokenness into raw grace & unconditional love!
- Discover how you, right now, can change the world!

Target Market(s)

Church members and people outside the church looking for an equipping process.

Industry/Entity Type

Church

Font styles to use
Serif
Sans Serif
Decorative
Script

Colors

Designer to choose colors to be used in the design.

Requirements
Must have
• Logo of our church. Overall concept of Summit Path throughout and each class represented uniquely in the concept. Summit Path is the overall process, but it is also the first class.

```html
<!DOCTYPE html>
<html lang="en">
<head>
<meta charset="utf-8">
<title>Summit Path Banner</title>
<link href="https://fonts.googleapis.com/css2?family=Oswald:wght@500;700&family=Arimo:wght@400;700&family=Tinos:ital@1&family=Open+Sans:wght@300;400&family=Dancing+Script:wght@600&display=swap" rel="stylesheet">
<style>
  :root {
    --stage: #b4b6b9;
    --paper: #ffffff;
    --ink: #2b2b2d;
    --ink-soft: #4a4a4d;
    --accent-blue: #2f6db3;
    --yellow: #f7d234;
    --orange: #f7a623;
    --green: #8cc54a;
    --purple: #c178c5;
    --pink: #ec78b0;
    --lavender: #9497cf;
    --sky: #3aaee3;
    --band: #e1e2e4;
  }
  * { margin: 0; padding: 0; box-sizing: border-box; }
  html, body { width: 1200px; height: 1000px; overflow: hidden; }
  body {
    background: radial-gradient(circle at 50% 50%, #d2d3d5 0%, var(--stage) 70%, #9d9fa2 100%);
    position: relative;
    font-family: "Arimo", Arial, sans-serif;
    color: var(--ink);
  }
  .banner {
    position: absolute; left: 302px; top: 50px;
    width: 596px; height: 898px;
    background: var(--paper);
  }
  .church-name {
    position: absolute; left: 16px; top: 26px;
    display: flex; align-items: center; gap: 6px;
    font-family: "Oswald", sans-serif; font-weight: 500;
    color: var(--ink-soft); line-height: 1;
  }
  .church-name .dot { width: 22px; height: 22px; border-radius: 50%; background: var(--ink-soft); }
  .church-name .name { font-size: 22px; letter-spacing: 1px; }
  .church-name .sub { font-size: 7px; letter-spacing: 1.6px; display: block; margin-top: 2px; }
  .mission {
    position: absolute; right: 14px; top: 24px; text-align: right;
    font-family: "Tinos", serif; font-style: italic; color: var(--ink-soft);
  }
  .mission .line { font-size: 15px; }
  .mission .line b { font-family: "Arimo", sans-serif; font-style: normal; color: var(--accent-blue); font-size: 17px; }
  .mission .verse { font-size: 9px; margin-top: 3px; }
  .wheel { position: absolute; left: 0; top: 0; }
  .seg-label { font-family: "Oswald", sans-serif; font-weight: 700; fill: var(--ink); text-anchor: middle; }
  .hub-title { font-family: "Open Sans", sans-serif; font-weight: 300; font-size: 38px; fill: var(--ink); text-anchor: middle; }
  .hub-tag { font-family: "Open Sans", sans-serif; font-size: 8px; fill: var(--ink-soft); text-anchor: middle; }
  .icon { fill: none; stroke: var(--ink); stroke-width: 2.4; stroke-linecap: round; stroke-linejoin: round; }
  .benefits { position: absolute; left: 0; top: 588px; width: 100%; text-align: center; }
  .benefits h2 { font-weight: 400; font-size: 28px; color: var(--ink); }
  .benefits h2 span { color: var(--accent-blue); }
  .benefits ul { list-style: none; margin-top: 6px; font-weight: 700; font-size: 10.4px; line-height: 13.5px; color: var(--ink); }
  .people-photo {
    position: absolute; left: 16px; top: 680px; width: 564px; height: 156px;
    background: linear-gradient(90deg, #eae6e2 0%, #c9b8a8 20%, #e8d6c6 45%, #d2b8a2 65%, #a8463f 78%, #e6d3b8 100%);
  }
  .pillars {
    position: absolute; left: 0; bottom: 0; width: 100%; height: 60px;
    background: var(--band); display: flex; justify-content: center; gap: 58px; padding-top: 12px;
  }
  .pillar { width: 118px; position: relative; }
  .pillar .kicker { font-family: "Dancing Script", cursive; font-size: 9px; color: var(--accent-blue); display: block; margin-left: 26px; line-height: 1; }
  .pillar .word { display: flex; align-items: center; gap: 3px; font-family: "Oswald", sans-serif; font-weight: 700; font-size: 19px; line-height: 1; color: var(--ink); }
  .pillar p { font-size: 4.6px; font-weight: 700; line-height: 5.6px; color: var(--ink-soft); text-transform: uppercase; margin-top: 2px; margin-left: 26px; }
</style>
</head>
<body>
<main class="banner">
  <div class="church-name">
    <span class="dot"></span>
    <span><span class="name">BRENLUX</span><span class="sub">INTERNATIONAL OUTREACH</span></span>
  </div>
  <div class="mission">
    <div class="line">Teaching People, Reaching Nations with <b>Freedom.</b></div>
    <div class="verse">Galatians 5:1</div>
  </div>

  <svg class="wheel" width="596" height="590" viewBox="0 0 596 590" aria-label="Seven steps of Summit Path">
    <defs>
      <path id="sector" d="M -47.8 -115.5 L -78.5 -189.4 A 205 205 0 0 1 78.5 -189.4 L 47.8 -115.5 A 125 125 0 0 0 -47.8 -115.5 Z"/>
    </defs>
    <g transform="translate(298 322)">
      <!-- Make Jesus Famous -->
      <g transform="rotate(292.5)">
        <path d="M -88.4 -88.4 L -180.3 -180.3 A 255 255 0 0 1 180.3 -180.3 L 88.4 -88.4 A 125 125 0 0 0 -88.4 -88.4 Z" fill="var(--sky)" stroke="#fff" stroke-width="2"/>
        <text class="seg-label" y="-188" font-size="20">MAKE JESUS</text>
        <text class="seg-label" y="-152" font-size="38">FAMOUS</text>
        <g class="icon" transform="translate(-120 -196) rotate(-30)">
          <path d="M -10 -5 L 8 -13 L 8 13 L -10 5 Z"/><path d="M -10 -5 L -14 -5 L -14 5 L -10 5"/><path d="M -8 5 L -5 14"/>
        </g>
      </g>
      <!-- Find Your Identity -->
      <g>
        <use href="#sector" fill="var(--yellow)" stroke="#fff" stroke-width="2"/>
        <circle cy="-205" r="44" fill="var(--yellow)"/>
        <text class="seg-label" y="-175" font-size="16">FIND YOUR</text>
        <text class="seg-label" y="-147" font-size="27">IDENTITY</text>
        <g class="icon" transform="translate(0 -215)" stroke-width="1.6">
          <circle r="4"/><circle r="8"/><circle r="12"/><path d="M -16 4 A 16 16 0 0 1 16 4"/>
        </g>
      </g>
      <!-- Realign with Harvest Rhythm -->
      <g transform="rotate(45)">
        <use href="#sector" fill="var(--orange)" stroke="#fff" stroke-width="2"/>
        <circle cy="-205" r="44" fill="var(--orange)"/>
        <text class="seg-label" y="-180" font-size="13">REALIGN WITH</text>
        <text class="seg-label" y="-158" font-size="22">HARVEST</text>
        <text class="seg-label" y="-136" font-size="22">RHYTHM</text>
        <g class="icon" transform="translate(22 -215)">
          <path d="M -14 8 L -16 -8 L -7 0 L 0 -12 L 7 0 L 16 -8 L 14 8 Z"/><path d="M -14 13 L 14 13"/>
        </g>
      </g>
      <!-- Engage in Spiritual Community -->
      <g transform="rotate(90)">
        <use href="#sector" fill="var(--green)" stroke="#fff" stroke-width="2"/>
        <circle cy="-205" r="44" fill="var(--green)"/>
        <text class="seg-label" y="-180" font-size="16">ENGAGE IN</text>
        <text class="seg-label" y="-160" font-size="16">SPIRITUAL</text>
        <text class="seg-label" y="-140" font-size="16">COMMUNITY</text>
        <g class="icon" transform="translate(0 -222) rotate(-90)">
          <path d="M 0 12 L -13 -1 A 7 7 0 0 1 0 -9 A 7 7 0 0 1 13 -1 Z"/>
        </g>
      </g>
      <!-- Explore Your Creative Design -->
      <g transform="rotate(135)">
        <use href="#sector" fill="var(--purple)" stroke="#fff" stroke-width="2"/>
        <circle cx="-22" cy="-205" r="44" fill="var(--purple)"/>
        <text class="seg-label" y="-180" font-size="13">EXPLORE YOUR</text>
        <text class="seg-label" y="-160" font-size="18">CREATIVE</text>
        <text class="seg-label" y="-136" font-size="26">DESIGN</text>
        <g class="icon" transform="translate(-24 -215) rotate(-135)">
          <circle cy="-3" r="9"/><path d="M -4 7 L 4 7 M -3 11 L 3 11"/>
        </g>
      </g>
      <!-- Demonstrate the Power of the Spirit -->
      <g transform="rotate(180)">
        <use href="#sector" fill="var(--pink)" stroke="#fff" stroke-width="2"/>
        <circle cy="-205" r="44" fill="var(--pink)"/>
        <text class="seg-label" y="-180" font-size="12">DEMONSTRATE THE</text>
        <text class="seg-label" y="-160" font-size="18">POWER OF</text>
        <text class="seg-label" y="-138" font-size="18">THE SPIRIT</text>
        <g class="icon" transform="translate(0 -218)">
          <circle r="4"/><circle r="9"/><circle r="14"/>
        </g>
      </g>
      <!-- Open Your Heart to the Poor -->
      <g transform="rotate(225)">
        <use href="#sector" fill="var(--lavender)" stroke="#fff" stroke-width="2"/>
        <circle cx="22" cy="-205" r="44" fill="var(--lavender)"/>
        <text class="seg-label" y="-172" font-size="30">OPEN</text>
        <text class="seg-label" y="-152" font-size="16">YOUR HEART</text>
        <text class="seg-label" y="-135" font-size="14">TO THE POOR</text>
        <g class="icon" transform="translate(26 -215) rotate(135)">
          <path d="M -12 -5 L -6 -12 L 6 -12 L 12 -5 L 0 12 Z"/><path d="M -12 -5 L 12 -5 M -6 -12 L 0 12 L 6 -12"/>
        </g>
      </g>
      <!-- Hub -->
      <circle r="133" fill="#fff"/>
      <text class="hub-title" y="12">Summit Path</text>
      <text class="hub-tag" y="34">Discovering Who I Am, What I'm Created to Do, &amp; How to Do It</text>
    </g>
  </svg>

  <section class="benefits">
    <h2>What Will <span>Summit Path</span> Do For You?</h2>
    <ul>
      <li>Encounter The Radical Grace &amp; Supernatural Love of Your Heavenly Father!</li>
      <li>Learn Something Practical And Relevant That's Guaranteed to Work On Sunday And Monday!</li>
      <li>Connect With Others Like You-People Walking From Brokenness Into Raw Grace &amp; Unconditional Love!</li>
      <li>Discover How You, Right Now, Can Change The World!</li>
    </ul>
  </section>

  <div class="people-photo" role="img" aria-label="Photo of five young adults seated in a row, talking and reading books together"></div>

  <footer class="pillars">
    <div class="pillar">
      <span class="kicker">The outcome</span>
      <div class="word"><svg width="23" height="23" viewBox="-12 -12 24 24"><circle r="11" fill="var(--ink)"/><circle r="7" fill="none" stroke="#fff" stroke-width="1.2"/><circle r="3" fill="none" stroke="#fff" stroke-width="1.2"/></svg>FREEDOM</div>
      <p>Radical grace moves us beyond guilt, shame, sin, addiction and hurts.</p>
    </div>
    <div class="pillar">
      <span class="kicker">Our message</span>
      <div class="word">CONNECT<svg width="23" height="20" viewBox="-12 -10 24 20"><path d="M -8 -3 L 8 -9 L 8 9 L -8 3 Z M -8 -3 L -11 -3 L -11 3 L -8 3 M -6 3 L -4 9" fill="none" stroke="var(--ink)" stroke-width="2" stroke-linejoin="round"/></svg></div>
      <p>Radical grace connects us to the Father, to each other and the world.</p>
    </div>
    <div class="pillar">
      <span class="kicker">The beginning, middle, &amp; end</span>
      <div class="word"><svg width="22" height="20" viewBox="-12 -10 24 20"><path d="M -9 5 L -10 -7 L -4 -1 L 0 -9 L 4 -1 L 10 -7 L 9 5 Z M -9 9 L 9 9" fill="none" stroke="var(--ink)" stroke-width="2" stroke-linejoin="round"/></svg>JESUS</div>
      <p>The finished work of Jesus makes it all possible for us.</p>
    </div>
  </footer>
</main>
</body>
</html>
```